Process Roadmap for Interior Design Firm

We are looking to ramp up the design appeal of our current process roadmap to be very visually interesting, while staying informative and descriptive about our process.

Target Market(s)

In-house Clients

Industry/Entity Type

Interior Design Firm focused on sustainable and holistic design.

Other font styles liked:
• raleway

Requirements
Must have
• 1.) it would be nice if the graphic provided a more clear indication of the “journey” from one step to the next, so that there was a clear sense of the progression (such that we are directing the viewer) 2.). We would want it to fit on an 8.5”x11” page (the page could be horizontal when we have the Calm Compass formatted out with the testimonials) (in addition to the testimonials, we may also want to have the detailed descriptions of each step of the process presented below the graphic, so that the graphic is cleaner) 3.) ideally the graphic is clear and simple enough to also be used on our Bi-Weekly Client Updates, which will be typed updates for clients re their project budgets, schedule and scope. The Calm Compass graphic (without all the testimonials) would be at the end of the update, and would fit on the page horizontally at the bottom, perhaps in a space which is 7.5”w x 4”h or so.
Should not have
• bold or bright colors. Natural neutrals are preferred, such as the ones featured on the provided graphic.

```html
<!DOCTYPE html>
<html lang="en">
<head>
<meta charset="utf-8">
<title>Calm Compass – Process Roadmap</title>
<link href="https://fonts.googleapis.com/css2?family=Poppins:wght@300;500&display=swap" rel="stylesheet">
<style>
  :root{
    --bg:#ffffff;
    --panel:#f8f9fa;
    --band:#d5bda3;
    --ring:#d8c4ae;
    --body-text:#555555;
    --listening:#646d4f;
    --visioning:#9b9985;
    --planning:#fcebde;
    --designing:#e2d1be;
    --managing:#cba68c;
    --installing:#b39b84;
    --completing:#b0ac85;
    --label-light:#ffffff;
    --label-dark:#222222;
  }
  html,body{margin:0;padding:0;overflow:hidden;background:var(--bg);}
  .roadmap{position:relative;width:1200px;height:927px;overflow:hidden;font-family:"Poppins",sans-serif;}
  .step-note{
    position:absolute;width:203px;border-radius:26px;
    font-weight:300;font-size:14.2px;line-height:20.4px;color:var(--body-text);
    box-sizing:border-box;
  }
  .step-note--above{background:linear-gradient(to bottom,var(--panel),#fdfdfd);}
  .step-note--below{background:linear-gradient(to bottom,#fdfdfd,var(--panel));}
  .step-note p{margin:0;}
  .route{position:absolute;left:0;top:0;}
  .stage-label{font-family:"Poppins",sans-serif;font-weight:500;font-size:16.5px;text-anchor:middle;dominant-baseline:middle;}
</style>
</head>
<body>
<div class="roadmap">

  <div class="step-note step-note--below" style="left:11px;top:319px;height:161px;padding:0 0 0 28px;">
    <p style="margin-top:0">Listening to our<br>clients, their land, and<br>their home.<br>Identifying their<br>needs, challenges,<br>wishes, and dreams.</p>
  </div>
  <div class="step-note step-note--above" style="left:152px;top:27px;height:216px;padding:36px 0 0 27px;">
    <p>Facilitating a guided<br>visioning process to<br>clarify the deepest<br>intention, true purpose,<br>and highest potential<br>for their home and<br>their future within it.</p>
  </div>
  <div class="step-note step-note--below" style="left:321px;top:300px;height:203px;padding:13px 0 0 17px;">
    <p>Turning our client's vision<br>into a clearly defined<br>scope, budget, and<br>timeline. Mapping out the<br>steps for making their<br>dream a reality. Setting a<br>meeting schedule from<br>start to finish.</p>
  </div>
  <div class="step-note step-note--above" style="left:482px;top:23px;height:220px;padding:24px 0 0 21px;">
    <p>Following the schedule<br>through the design<br>phases from initial<br>design concepts,<br>technical drawings and<br>details, and the selection<br>of all finishes, fixtures, and<br>surnishings.</p>
  </div>
  <div class="step-note step-note--below" style="left:647px;top:300px;height:203px;padding:9px 0 0 17px;">
    <p>Coordinating with clients,<br>builders, architects, and<br>vendors to ensure that<br>the design is executed<br>with excellence, and the<br>construction and<br>furnishings are on-time<br>and on-budget.</p>
  </div>
  <div class="step-note step-note--above" style="left:812px;top:24px;height:219px;padding:30px 0 0 24px;">
    <p>Overseeing the<br>inspection, installation,<br>and arrangement of all<br>furnishings, lighting,<br>artwork, and decorative<br>items. Taking care of<br>every last detail.</p>
  </div>
  <div class="step-note step-note--below" style="left:984px;top:297px;height:181px;padding:13px 0 0 19px;">
    <p>Fixing any issues or<br>defects. Follow up on all<br>remaining items.<br>Completing the final<br>finishing touches to our<br>client's full and total<br>satisfaction.</p>
  </div>

  <svg class="route" width="1200" height="927" viewBox="0 0 1200 927">
    <defs>
      <marker id="arrow-tip" viewBox="0 0 10 10" refX="8" refY="5" markerWidth="4" markerHeight="4" orient="auto">
        <path d="M0 0 L10 5 L0 10 z" fill="#ffffff"/>
      </marker>
    </defs>

    <path d="M89 213 L254 308 L419 213 L584 308 L749 213 L914 308 L1079 213"
          fill="none" stroke="var(--band)" stroke-width="46" stroke-linejoin="round"/>

    <g stroke="#ffffff" stroke-width="1.6" marker-end="url(#arrow-tip)">
      <line x1="150" y1="249" x2="189" y2="273"/>
      <line x1="316" y1="272" x2="355" y2="249"/>
      <line x1="483" y1="250" x2="522" y2="274"/>
      <line x1="645" y1="272" x2="684" y2="249"/>
      <line x1="812" y1="250" x2="851" y2="274"/>
      <line x1="974" y1="272" x2="1014" y2="249"/>
    </g>

    <g fill="#ffffff" stroke="var(--ring)" stroke-width="1.4">
      <circle cx="89" cy="213" r="65"/>
      <circle cx="254" cy="308" r="65"/>
      <circle cx="419" cy="213" r="65"/>
      <circle cx="584" cy="308" r="65"/>
      <circle cx="749" cy="213" r="65"/>
      <circle cx="914" cy="308" r="65"/>
      <circle cx="1079" cy="213" r="65"/>
    </g>

    <circle cx="89" cy="213" r="56" fill="var(--listening)"/>
    <circle cx="254" cy="308" r="56" fill="var(--visioning)"/>
    <circle cx="419" cy="213" r="56" fill="var(--planning)"/>
    <circle cx="584" cy="308" r="56" fill="var(--designing)"/>
    <circle cx="749" cy="213" r="56" fill="var(--managing)"/>
    <circle cx="914" cy="308" r="56" fill="var(--installing)"/>
    <circle cx="1079" cy="213" r="56" fill="var(--completing)"/>

    <text class="stage-label" x="89" y="214" fill="var(--label-light)">LISTENING</text>
    <text class="stage-label" x="254" y="309" fill="var(--label-light)">VISIONING</text>
    <text class="stage-label" x="419" y="215" fill="var(--label-dark)">PLANNING</text>
    <text class="stage-label" x="584" y="310" fill="var(--label-dark)">DESIGNING</text>
    <text class="stage-label" x="749" y="214" fill="var(--label-light)">MANAGING</text>
    <text class="stage-label" x="914" y="310" fill="var(--label-light)">INSTALLING</text>
    <text class="stage-label" x="1079" y="214" fill="var(--label-light)">COMPLETING</text>

    <g fill="none" stroke="var(--ring)" stroke-width="2.2" stroke-linecap="round" stroke-linejoin="round">
      <polyline points="79,286 86,293 93,286"/>
      <polyline points="417,286 424,293 431,286"/>
      <polyline points="745,286 752,293 759,286"/>
      <polyline points="1076,286 1083,293 1090,286"/>
      <polyline points="244,233 251,226 258,233"/>
      <polyline points="576,233 583,226 590,233"/>
      <polyline points="908,233 915,226 922,233"/>
    </g>
  </svg>

</div>
</body>
</html>
```